Real EState

A real estate company. I want to start a mailing of 1,000 standard size post cards. I want to mail these every month. Starting Jan 2015. The first 1,000 talking about this new year, the following months something to do with the seasons or holidays upcoming. I would like the design to be familiar each month so that my company will be recognized. I can send you my business card and logo which has my address phone# etc. I only want to spend the $29 design change each month, not the $180. I believe this should be attainable knowing I want consistency, I want my clients to easily know who my company is and I am available to help them get their real estate needs accomplished. One phrase I would like them to read each time is this. Why don't you take this opportunity now and give me a call or stop by because " When you open our door, it will definitely open doors for you.

I am not good at this type communication. I would really like to speak to someone. I know we cannot so please bare with me. I have no idea if my brief has gone out to everyone or not. here is what I would like. My logo needs to be there. The letters K&D PROPERTIES needs to be in gold. The buildings and lines going across need to be a light gray. I would like to see a nice quality door along with maybe a side light window. There needs to be a key in the door. I would like to see the door opening. I also want the phrase that I sent to everyone regarding opening the door. All other colors need to blend in with the colors of the logo. Lets put in all the phone numbers on the business card along with the e-mail address. Please at this time leave off the web address until I can update the site.

Reason: I am not good at this kind of communication. My computer skills are not good enough to even understand the programs your using. I don't even know if everyone is getting my explanations or even the feed back. Every time I try to bring up a design I lose the page in front of me I think I am getting better working your system but time will tell. Please bare with me. I will be loyal to the designer that can give what I need but again I'm having a hard time knowing who's who and keeping track of them.

Industry/Entity Type

Real Estate

```html
<!DOCTYPE html>
<html lang="en">
<head>
<meta charset="utf-8">
<title>K&amp;D Properties Postcard</title>
<link rel="stylesheet" href="https://fonts.googleapis.com/css2?family=Tinos:wght@400;700&family=Oswald:wght@500;600&family=Lato:wght@400;700&display=swap">
<style>
  :root {
    --bg: #2a2a2a;
    --green: #1f8a3a;
    --green-dark: #136b2a;
    --green-light: #2fa34a;
    --red: #d0202a;
    --red-dark: #9e141c;
    --gold: #f2b51c;
    --white: #ffffff;
    --ink: #222222;
    --rule: #555555;
  }
  * { margin: 0; padding: 0; box-sizing: border-box; }
  html, body { width: 797px; height: 1200px; overflow: hidden; }
  body { background: var(--bg); position: relative; font-family: "Tinos", serif; }

  .card { position: absolute; overflow: hidden; }
  .card-front { left: 75px; top: 60px; width: 652px; height: 508px;
    background: radial-gradient(ellipse at 40% 80%, var(--green-light), var(--green-dark) 75%); }
  .card-back { left: 75px; top: 635px; width: 660px; height: 505px; background: var(--white); }
  .card svg.shapes { position: absolute; inset: 0; }

  .brand-name { position: absolute; left: 18px; top: 18px; width: 140px;
    font-family: "Tinos", serif; font-weight: 700; font-size: 17px; line-height: 1.1;
    color: var(--gold); }

  .phone-tag { position: absolute; left: 430px; top: 332px; width: 200px; height: 40px;
    background: var(--red); display: flex; align-items: center; gap: 10px; padding-left: 28px;
    clip-path: polygon(0 0, 100% 0, 100% 100%, 0 100%, 8% 50%); }
  .phone-tag span { font-family: "Tinos", serif; font-size: 24px; color: var(--gold); }

  .invite { position: absolute; right: 28px; top: 382px; text-align: right; white-space: nowrap;
    font-family: "Tinos", serif; font-weight: 700; font-size: 21px; line-height: 27px; color: var(--white); }
  .slogan { position: absolute; left: 0; right: 0; top: 446px; text-align: center; white-space: nowrap;
    font-family: "Oswald", sans-serif; font-weight: 600; font-size: 27px; line-height: 36px;
    color: var(--red); text-shadow: 0 0 6px rgba(255,255,255,0.35); }

  .ribbon { position: absolute; height: 34px; background: var(--red);
    font-family: "Oswald", sans-serif; font-weight: 500; font-size: 20px; color: var(--gold);
    display: flex; align-items: center; padding-left: 22px; white-space: nowrap; }
  .ribbon-about { left: 0; top: 30px; width: 238px; clip-path: polygon(0 0, 100% 0, 93% 50%, 100% 100%, 0 100%); }
  .ribbon-services { left: 0; top: 195px; width: 182px; clip-path: polygon(0 0, 100% 0, 90% 50%, 100% 100%, 0 100%); }
  .ribbon-contact { left: 70px; top: 333px; width: 200px; justify-content: center; padding-left: 0; }
  .ribbon-tail { position: absolute; top: 342px; width: 52px; height: 28px; background: var(--red-dark); }
  .ribbon-tail.left { left: 20px; clip-path: polygon(0 0, 100% 0, 100% 100%, 0 100%, 25% 50%); }
  .ribbon-tail.right { left: 268px; clip-path: polygon(0 0, 100% 0, 75% 50%, 100% 100%, 0 100%); }

  .about-text { position: absolute; left: 24px; top: 70px; width: 334px;
    font-family: "Tinos", serif; font-weight: 700; font-size: 14px; line-height: 19.5px;
    color: var(--white); text-align: justify; }

  .services { position: absolute; left: 22px; top: 240px; width: 300px; list-style: none;
    display: grid; grid-template-columns: 155px 145px; row-gap: 2px;
    font-family: "Tinos", serif; font-weight: 700; font-size: 17px; color: var(--white); }
  .services li { display: flex; align-items: center; gap: 6px; height: 22px; white-space: nowrap; }

  .contact { position: absolute; left: 0; top: 382px; width: 340px; text-align: center; color: var(--white); font-family: "Lato", sans-serif; }
  .contact .name { font-weight: 700; font-size: 21px; color: var(--gold); letter-spacing: 0.5px; }
  .contact .role { font-size: 17px; margin-top: 2px; }
  .contact .line { font-size: 12px; margin-top: 4px; display: flex; align-items: center; justify-content: center; gap: 6px; white-space: nowrap; }

  .badge { position: absolute; top: 38px; height: 28px; background: var(--white); border: 1.5px solid var(--ink); }
  .badge-one { left: 385px; width: 26px; }
  .badge-two { left: 416px; width: 54px; }
  .stamp-box { position: absolute; left: 563px; top: 22px; width: 63px; height: 72px; border: 1.5px solid var(--ink); }
  .address-line { position: absolute; left: 398px; width: 232px; height: 1.5px; background: var(--rule); }
</style>
</head>
<body>

<section class="card card-front">
  <svg class="shapes" width="652" height="508" viewBox="0 0 652 508">
    <defs>
      <linearGradient id="doorPhoto" x1="0" y1="0" x2="1" y2="0">
        <stop offset="0" stop-color="#c9d8b0"/>
        <stop offset="0.3" stop-color="#9cc06a"/>
        <stop offset="0.52" stop-color="#6a5a4c"/>
        <stop offset="0.7" stop-color="#3a2a24"/>
        <stop offset="1" stop-color="#5a4036"/>
      </linearGradient>
    </defs>
    <path role="img" aria-label="Photo of an opening front door with handle and side window" fill="url(#doorPhoto)"
      d="M0,150 Q90,25 330,0 L652,0 L652,290 Q520,330 420,370 Q240,420 0,410 Z"/>
    <path d="M0,150 Q90,25 330,0" fill="none" stroke="#fff" stroke-width="3"/>
    <path d="M0,358 Q300,420 652,228" fill="none" stroke="#fff" stroke-width="2"/>
    <path d="M0,410 Q240,420 420,370 Q520,330 652,290" fill="none" stroke="#fff" stroke-width="3"/>
  </svg>
  <div class="brand-name">K&amp;D<br>PROPERTIES</div>
  <div class="phone-tag">
    <svg width="12" height="18" viewBox="0 0 12 18"><rect x="1" y="1" width="10" height="16" rx="2" fill="none" stroke="#f2b51c" stroke-width="1.8"/><rect x="3.5" y="4" width="5" height="6" fill="#f2b51c"/></svg>
    <span>248.555.0172</span>
  </div>
  <p class="invite">Why don't you take<br>this opportunity now &amp; give me a call or stop by because</p>
  <p class="slogan">WHEN YOU OPEN OUR DOOR, IT WILL DEFINITELY OPEN</p>
</section>

<section class="card card-back">
  <svg class="shapes" width="660" height="505" viewBox="0 0 660 505">
    <defs>
      <radialGradient id="backGreen" cx="0.4" cy="0.45" r="0.7">
        <stop offset="0" stop-color="#2fa34a"/>
        <stop offset="1" stop-color="#136b2a"/>
      </radialGradient>
    </defs>
    <path fill="#d0202a" d="M0,0 L362,0 Q400,40 395,130 Q387,260 355,340 Q335,420 368,505 L0,505 Z"/>
    <path fill="#f2b51c" d="M0,0 L352,0 Q390,40 385,130 Q377,260 345,340 Q325,420 358,505 L0,505 Z"/>
    <path fill="url(#backGreen)" d="M0,0 L342,0 Q380,40 375,130 Q367,260 335,340 Q315,420 348,505 L0,505 Z"/>
  </svg>

  <div class="ribbon ribbon-about">ABOUT K&amp;D PROPERTIES</div>
  <p class="about-text">Lorem ipsum dolor sit amet, consectetuer adipscng elit, sed diam nonummy nibh euismod tincidunt ut laoreet dolore magna aliquam erat volutpat. Ut wisi enim ad minim veniam, quis nostrud exerci tation ullmcorper suscipit lobortis nisl ut aliquip ex ea commodo consequat.</p>

  <div class="ribbon ribbon-services">OUR SERVICES</div>
  <ul class="services">
    <li><svg width="14" height="14" viewBox="0 0 14 14"><path d="M1,7 L5,11 L13,2" fill="none" stroke="#f2b51c" stroke-width="3"/></svg>Lorem ipsum</li>
    <li><svg width="14" height="14" viewBox="0 0 14 14"><path d="M1,7 L5,11 L13,2" fill="none" stroke="#f2b51c" stroke-width="3"/></svg>Lorem ipsum</li>
    <li><svg width="14" height="14" viewBox="0 0 14 14"><path d="M1,7 L5,11 L13,2" fill="none" stroke="#f2b51c" stroke-width="3"/></svg>Lorem ipsum</li>
    <li><svg width="14" height="14" viewBox="0 0 14 14"><path d="M1,7 L5,11 L13,2" fill="none" stroke="#f2b51c" stroke-width="3"/></svg>Lorem ipsum</li>
    <li><svg width="14" height="14" viewBox="0 0 14 14"><path d="M1,7 L5,11 L13,2" fill="none" stroke="#f2b51c" stroke-width="3"/></svg>Lorem ipsum</li>
  </ul>

  <div class="ribbon-tail left"></div>
  <div class="ribbon-tail right"></div>
  <div class="ribbon ribbon-contact">CONTACT US</div>

  <div class="contact">
    <p class="name">MARCUS T. HALE JR.</p>
    <p class="role">Broker &amp; Consultant</p>
    <p class="line"><svg width="10" height="10" viewBox="0 0 10 10"><path d="M2,1 L4,1 L4.5,3.5 L3.3,4.3 Q4.5,6.2 5.7,6.7 L6.5,5.5 L9,6 L9,8 Q5,9.5 1,2.5 Z" fill="#d0202a"/></svg>248.555.0139</p>
    <p class="line"><svg width="11" height="8" viewBox="0 0 11 8"><rect width="11" height="8" rx="1" fill="#d0202a"/><path d="M0.5,0.8 L5.5,4.5 L10.5,0.8" fill="none" stroke="#fff" stroke-width="0.9"/></svg>marcushale@kd-properties.com</p>
    <p class="line"><svg width="9" height="9" viewBox="0 0 9 9"><circle cx="4.5" cy="4.5" r="4.5" fill="#d0202a"/></svg>415 N. Cedar Bend Rd. Oakvale, MI 48390</p>
  </div>

  <div class="badge badge-one"></div>
  <div class="badge badge-two"></div>
  <div class="stamp-box"></div>
  <div class="address-line" style="top:228px"></div>
  <div class="address-line" style="top:296px"></div>
  <div class="address-line" style="top:365px"></div>
</section>

</body>
</html>
```